Garden Design Flier

I would like a PDF of this half page A4 flier in soft green tones with dark green leaves.

Target Market(s)

Home owners and real estate agents

Font styles to use
Serif
Other font styles liked:
• Papyrus

Colors
acd136
9bcb3c
cadf82
fefdec

Requirements
Must have
• Green tones
Nice to have
• Leaves, vines, lawns
Should not have
• Open to ideas, but classic style

```html
<!DOCTYPE html>
<html lang="en">
<head>
<meta charset="utf-8">
<title>Garden Design Flier</title>
<link href="https://fonts.googleapis.com/css2?family=Macondo&family=Tinos:ital,wght@0,400;0,700;1,400&family=Montserrat:wght@700&display=swap" rel="stylesheet">
<style>
  :root {
    --board: #2a2a2a;
    --title: #ffffff;
    --olive: #4b5a22;
    --ink: #2b2b22;
    --paper: #ffffff;
    --leaf-pale: #eef4dc;
    --leaf-soft: #d6e6ae;
    --leaf-mid: #bfd58c;
    --leaf-sage: #c9cfb4;
    --cream: #fefdec;
  }
  html, body {
    margin: 0;
    padding: 0;
    overflow: hidden;
  }
  .board {
    position: relative;
    width: 1200px;
    height: 487px;
    background: var(--board);
    overflow: hidden;
  }
  .board-title {
    position: absolute;
    top: 26px;
    left: 0;
    right: 0;
    margin: 0;
    text-align: center;
    font-family: "Tinos", "Times New Roman", serif;
    font-weight: 400;
    font-size: 25px;
    line-height: 1;
    color: var(--title);
  }
  .flyer {
    position: absolute;
    top: 75px;
    width: 534px;
    height: 376px;
    overflow: hidden;
  }
  .flyer--script { left: 52px; }
  .flyer--serif { left: 620px; }
  .foliage-backdrop {
    position: absolute;
    inset: 0;
    width: 100%;
    height: 100%;
  }
  .frame {
    position: absolute;
    left: 47px;
    top: 34px;
    width: 441px;
    height: 309px;
    box-sizing: border-box;
    border: 4.5px solid var(--olive);
    background: var(--paper);
  }
  .frame > * {
    position: absolute;
    left: 0;
    right: 0;
    margin: 0;
    text-align: center;
    line-height: 1;
    white-space: nowrap;
  }
  .brand-name, .brand-sub, .services { color: var(--olive); }
  .owner, .credential, .pitch, .contact { color: var(--ink); }
  .rule {
    left: 21px;
    right: 21px;
    height: 0;
    border-top: 1px solid var(--olive);
    top: 271px;
  }
  .contact .sep { margin: 0 9px; }

  /* Papyrus-style variant */
  .flyer--script .frame > * { font-family: "Macondo", "Papyrus", fantasy; }
  .flyer--script .brand-name { top: 12px; font-size: 58px; letter-spacing: 0.03em; }
  .flyer--script .brand-sub { top: 72px; font-size: 16px; letter-spacing: 0.55em; padding-left: 0.55em; }
  .flyer--script .owner { top: 104px; font-size: 13px; }
  .flyer--script .credential { top: 124px; font-size: 12px; }
  .flyer--script .services { top: 161px; font-size: 21px; }
  .flyer--script .pitch { top: 199px; font-size: 12px; line-height: 18px; }
  .flyer--script .contact { top: 279px; font-size: 10px; }
  .flyer--script .rule { top: 271px; }

  /* Classic serif variant */
  .flyer--serif .frame > * { font-family: "Tinos", "Times New Roman", serif; }
  .flyer--serif .brand-name { top: 15px; font-size: 57px; letter-spacing: 0.08em; padding-left: 0.08em; }
  .flyer--serif .brand-sub { top: 70px; font-size: 21px; letter-spacing: 0.62em; padding-left: 0.62em; }
  .flyer--serif .owner { top: 103px; font-size: 12px; }
  .flyer--serif .credential { top: 123px; font-size: 13px; }
  .flyer--serif .services { top: 161px; font-size: 17px; }
  .flyer--serif .pitch { top: 202px; font-size: 12.5px; line-height: 15.5px; font-style: italic; }
  .flyer--serif .contact { top: 279px; font-size: 10.5px; }
  .flyer--serif .contact .sep { margin: 0 5px; }
</style>
</head>
<body>
<main class="board">
  <h1 class="board-title">Garden Design Flier</h1>

  <section class="flyer flyer--script">
    <svg class="foliage-backdrop" role="img" aria-label="Watercolour pattern of soft green and sage leaves and vines" viewBox="0 0 534 376" preserveAspectRatio="none">
      <defs>
        <linearGradient id="foliage-a" x1="0" y1="0" x2="1" y2="1">
          <stop offset="0" stop-color="var(--leaf-soft)"/>
          <stop offset="0.35" stop-color="var(--leaf-pale)"/>
          <stop offset="0.65" stop-color="var(--cream)"/>
          <stop offset="1" stop-color="var(--leaf-mid)"/>
        </linearGradient>
      </defs>
      <rect width="534" height="376" fill="url(#foliage-a)"/>
    </svg>
    <div class="frame">
      <p class="brand-name">BRAMBLE</p>
      <p class="brand-sub">GARDENS</p>
      <p class="owner">by OWEN HARTLEY</p>
      <p class="credential">Certificate 3. Horticulture, Riverbend College, NSW</p>
      <p class="services">Design • Install • Grow • Tend • Enjoy</p>
      <p class="pitch">All your gardening and landscaping needs from design<br>and installation to general maintenance Bespoke vegetable gardens<br>and potager designscreated to suite youe site ans requirements</p>
      <div class="rule"></div>
      <p class="contact">email: owen@bramblegardens.com.au<span class="sep">|</span>Call : 0400-318452<span class="sep">|</span>ABN:51902736418</p>
    </div>
  </section>

  <section class="flyer flyer--serif">
    <svg class="foliage-backdrop" role="img" aria-label="Watercolour pattern of soft green and sage leaves and vines" viewBox="0 0 534 376" preserveAspectRatio="none">
      <defs>
        <linearGradient id="foliage-b" x1="0" y1="0" x2="1" y2="1">
          <stop offset="0" stop-color="var(--leaf-soft)"/>
          <stop offset="0.35" stop-color="var(--leaf-pale)"/>
          <stop offset="0.65" stop-color="var(--cream)"/>
          <stop offset="1" stop-color="var(--leaf-mid)"/>
        </linearGradient>
      </defs>
      <rect width="534" height="376" fill="url(#foliage-b)"/>
    </svg>
    <div class="frame">
      <p class="brand-name">BRAMBLE</p>
      <p class="brand-sub">GARDENS</p>
      <p class="owner">by OWEN HARTLEY</p>
      <p class="credential">Certificate 3. Horticulture, Riverbend College, NSW</p>
      <p class="services">DESIGN • INSTALL • GROW • TEND • ENJOY</p>
      <p class="pitch">All your gardening and landscaping needs from design<br>and installation to general maintenance Bespoke vegetable gardens<br>and potager designscreated to suite youe site ans requirements</p>
      <div class="rule"></div>
      <p class="contact">email: owen@bramblegardens.com.au<span class="sep">|</span>Call : 0400-318452<span class="sep">|</span>ABN:51902736418</p>
    </div>
  </section>
</main>
</body>
</html>
```